Robotic startup business cards

We are looking for a design for a set of business cards which reflect the spirit and humor of Vortalo Robotics. We want to present ourselves as sleek, professional, but laid-back consulting company.

We primarily focus on developing robotic arms software. This software controls robots and does things like grab items, pick objects up, move them, etc.

We want to allow you maximum design creativity, but do ask that you consider our existing style guidelines (see attached files) in order to make our brand cohesive.

Target Market(s)

Startups and Mid-size robotic companies

Industry/Entity Type

Business

Contact Information for Business Card

Miro Halvensky, PhD
Roboticist | Vortalo Consulting | 318.570.9164

Font styles to use
Other font styles liked:
• Source code pro

Requirements
Must have
• robots or robotic arms
• similar color scheme that works with existing brand guidelines
Nice to have
• please consider our existing style guidelines (see attached files) in order to make our brand cohesive.
• minimalism style is generally nice.
Should not have
• An old, boring, or corporate feel. Too much text.

```html
<!DOCTYPE html>
<html lang="en">
<head>
<meta charset="utf-8">
<title>Vortalo Consulting — Business Cards</title>
<link rel="stylesheet" href="https://fonts.googleapis.com/css2?family=Source+Code+Pro:wght@400;500;700&display=swap">
<style>
  :root {
    --bg: #e6e8eb;
    --card-dark: #050505;
    --card-light: #ffffff;
    --brand-green: #2fe08a;
    --ink: #111111;
    --ink-soft: #333333;
    --white: #ffffff;
    --shadow: 0 18px 40px rgba(0, 0, 0, 0.22);
  }
  * { box-sizing: border-box; margin: 0; padding: 0; }
  html, body {
    width: 1200px;
    height: 803px;
    overflow: hidden;
    background: var(--bg);
    font-family: "Source Code Pro", monospace;
  }
  .stage { position: relative; width: 1200px; height: 803px; }

  .card {
    position: absolute;
    width: 540px;
    height: 309px;
    border-radius: 22px;
    box-shadow: var(--shadow);
    overflow: hidden;
  }

  /* Front card */
  .card--front {
    left: 150px;
    top: 90px;
    background: var(--card-dark);
    display: flex;
    flex-direction: column;
    align-items: center;
    justify-content: center;
  }
  .brand-mark {
    display: flex;
    align-items: center;
    gap: 14px;
    color: var(--brand-green);
    font-weight: 700;
  }
  .brand-mark__square {
    width: 30px;
    height: 30px;
    background: var(--brand-green);
    border-radius: 4px;
  }
  .card--front .brand-mark { font-size: 38px; letter-spacing: 4px; margin-top: 20px; }
  .card__tagline {
    margin-top: 58px;
    color: var(--white);
    font-size: 11px;
    letter-spacing: 1.5px;
  }

  /* Back card */
  .card--back {
    left: 560px;
    top: 400px;
    background: var(--card-light);
    padding: 34px 40px;
  }
  .card--back .brand-mark { gap: 16px; }
  .card--back .brand-mark__square { width: 34px; height: 34px; }
  .brand-mark__name {
    font-size: 28px;
    font-weight: 500;
    letter-spacing: 5px;
    line-height: 1;
  }
  .brand-mark__sub {
    display: block;
    font-size: 13px;
    letter-spacing: 7px;
    margin-top: 4px;
  }

  .contact {
    position: absolute;
    right: 44px;
    top: 170px;
    list-style: none;
    font-size: 12px;
    font-weight: 500;
    color: var(--ink);
  }
  .contact__item { display: flex; align-items: center; gap: 10px; margin-bottom: 8px; }
  .contact__icon { width: 15px; height: 15px; flex: none; }

  .person {
    position: absolute;
    left: 90px;
    bottom: 40px;
  }
  .person__name { font-size: 17px; font-weight: 700; color: var(--ink); letter-spacing: 0.5px; }
  .person__title { font-size: 12px; font-weight: 500; color: var(--ink-soft); margin-top: 2px; }
</style>
</head>
<body>
<main class="stage">

  <section class="card card--front" aria-label="Business card front">
    <div class="brand-mark">
      <span class="brand-mark__square"></span>
      <span>VORTALO</span>
    </div>
    <p class="card__tagline">ROBOTIC SOFTWARE CONSULTANTS</p>
  </section>

  <section class="card card--back" aria-label="Business card back">
    <div class="brand-mark">
      <span class="brand-mark__square"></span>
      <span class="brand-mark__name">VORTALO<span class="brand-mark__sub">CONSULTING</span></span>
    </div>

    <ul class="contact">
      <li class="contact__item">
        <svg class="contact__icon" viewBox="0 0 24 24" fill="none" stroke="#2fe08a" stroke-width="2" stroke-linecap="round" stroke-linejoin="round" aria-hidden="true">
          <path d="M22 16.9v3a2 2 0 0 1-2.2 2 19.8 19.8 0 0 1-8.6-3.1 19.5 19.5 0 0 1-6-6A19.8 19.8 0 0 1 2.1 4.2 2 2 0 0 1 4.1 2h3a2 2 0 0 1 2 1.7c.1 1 .4 1.9.7 2.8a2 2 0 0 1-.5 2.1L8 9.9a16 16 0 0 0 6 6l1.3-1.3a2 2 0 0 1 2.1-.4c.9.3 1.8.6 2.8.7a2 2 0 0 1 1.7 2z"/>
        </svg>
        <span>318.570.9164</span>
      </li>
      <li class="contact__item">
        <svg class="contact__icon" viewBox="0 0 24 24" fill="none" stroke="#2fe08a" stroke-width="2" stroke-linejoin="round" aria-hidden="true">
          <rect x="2" y="5" width="20" height="14" rx="1.5"/>
          <path d="M2 6l10 7 10-7"/>
        </svg>
        <span>hello@vortalo.ai</span>
      </li>
    </ul>

    <div class="person">
      <p class="person__name">MIRO HALVENSKY,PhD</p>
      <p class="person__title">Roboticist</p>
    </div>
  </section>

</main>
</body>
</html>
```